New Body Mist 250 ml exclusive

We are excited to embark on a new project to design the packaging for body mist:
Amber Drizzle

We are looking for a design that is truly unique and stands out, with a touch of individuality that sets it apart. The design should be eye-catching and visually appealing, drawing attention even from a distance. We want the body mists to have a fun and attractive look that appeals to customers.

To help bring your design to life, we will provide the dimensions of the bottle, which has a capacity of 250ml. The bottle measures 13.3 cm in height and 4.9 cm in diameter (excluding the pump). Additionally, we will also provide the dimensions of the label, which measures 15.1 cm in height and 12.8 cm in width.

We believe that giving you the freedom to put your own unique touch and color choices will help create a truly standout design. We look forward to seeing your creative vision for our body mist.

We shared with you the logo of the body mist and some examples of models that we liked.

Please be informed that the project only includes one design and the remaining three will be completed and paid for through a 1on1 project with the winner of the contest.

Target Market(s)

Supermarket and perfumery stores

Industry/Entity Type

Cosmetics

Font styles to use
Serif

Requirements
Must have
• Uniqueness and attractiveness

```html
<!DOCTYPE html>
<html lang="en">
<head>
<meta charset="UTF-8">
<title>Velvet Always Body Mist Label</title>
<link rel="stylesheet" href="https://fonts.googleapis.com/css2?family=Allura&family=Playfair+Display:wght@700&family=Source+Sans+3:wght@300;400&display=swap">
<style>
  :root {
    --backdrop: #fde1e7;
    --label-wine: #650a22;
    --label-wine-deep: #5a081e;
    --gold: #c9a25c;
    --gold-soft: #d8b77a;
    --bloom-rose: #b8737f;
    --bloom-stem: #8a4a4c;
  }
  * { margin: 0; padding: 0; box-sizing: border-box; }
  html, body {
    width: 1200px;
    height: 1200px;
    overflow: hidden;
    background: var(--backdrop);
  }
  .canvas {
    position: relative;
    width: 1200px;
    height: 1200px;
    background: var(--backdrop);
  }
  .label {
    position: absolute;
    left: 260px;
    top: 199px;
    width: 680px;
    height: 802px;
    background: radial-gradient(ellipse at 60% 40%, var(--label-wine) 0%, var(--label-wine-deep) 100%);
    box-shadow: 0 2px 6px rgba(80, 10, 30, 0.25);
    overflow: hidden;
  }
  .label__title {
    position: absolute;
    left: 182px;
    top: 140px;
    font-family: "Allura", cursive;
    font-size: 128px;
    line-height: 0.86;
    color: var(--gold);
    font-weight: 400;
  }
  .label__title span { display: block; }
  .label__title .line-two { padding-left: 6px; }
  .label__bloom {
    position: absolute;
    left: 37px;
    top: 440px;
    width: 150px;
    height: 362px;
    background: linear-gradient(180deg, rgba(184,115,127,0.55) 0%, rgba(138,74,76,0.35) 60%, rgba(138,74,76,0.15) 100%);
    border-radius: 60px 60px 0 0;
  }
  .label__product-type {
    position: absolute;
    left: 0;
    width: 100%;
    top: 532px;
    padding-left: 10px;
    text-align: center;
    font-family: "Source Sans 3", sans-serif;
    font-weight: 300;
    font-size: 31px;
    color: var(--gold-soft);
  }
  .label__brand {
    position: absolute;
    left: 0;
    width: 100%;
    top: 668px;
    text-align: center;
    font-family: "Playfair Display", serif;
    font-weight: 700;
    font-size: 27px;
    color: var(--gold);
  }
  .label__volume {
    position: absolute;
    left: 289px;
    top: 724px;
    width: 103px;
    height: 34px;
    border: 1.5px solid var(--gold-soft);
    text-align: center;
    font-family: "Source Sans 3", sans-serif;
    font-weight: 400;
    font-size: 25px;
    line-height: 31px;
    color: var(--gold-soft);
  }
</style>
</head>
<body>
  <main class="canvas">
    <section class="label">
      <h1 class="label__title"><span class="line-one">Velvet</span><span class="line-two">Always</span></h1>
      <div class="label__bloom" role="img" aria-label="Line illustration of pink cosmos flowers on slender stems"></div>
      <p class="label__product-type">Body Mist</p>
      <p class="label__brand">Velvet Always</p>
      <p class="label__volume">250ml</p>
    </section>
  </main>
</body>
</html>
```